New Business Card Design Project

Updated business card design. I am moving towards more coaching of, for the most part women, who are searching for more in their lives. I am an intuitive healer, homeopath and nutritionist but also an author and motivational speaker. Int the past I have included my photo on the card but that is not essential. My book is called the Brilliance of Saffron - Reclaiming the Shade of Your Spirit so my colours are typically magenta.
Target Market(s)
Women - 35 - 60 considering improving their health. However, I am also a professional speaker with a target audience including corporate and conferences.
Industry/Entity Type
Health And Wellness
Contact Information for Business Card
Lucinda Parvell, CHN, RNCP, BSc
www.lucindaparvell.com
lucinda@lucindaparvell.com
519-362-7015
Facebook, instagram and twitter logos
Look and feel
Each slider illustrates characteristics of the customer's brand and the style your logo design should communicate.

```html
<!DOCTYPE html>
<html lang="en">
<head>
<meta charset="utf-8">
<title>Lucinda Parvell – Business Cards</title>
<link rel="stylesheet" href="https://fonts.googleapis.com/css2?family=Libre+Baskerville&family=Didact+Gothic&display=swap">
<style>
  :root {
    --backdrop: #262626;
    --card: #1c1c1d;
    --card-edge: #232324;
    --magenta: #e8197a;
    --ink: #f2f2f2;
    --logo-grey: #8a8a8c;
    --tagline-grey: #9a9a9c;
    --photo-warm: #c9a985;
    --photo-green: #5c7a3e;
    --social: #4f79a8;
  }
  * { box-sizing: border-box; margin: 0; padding: 0; }
  html, body { width: 1200px; height: 900px; overflow: hidden; background: var(--backdrop); }
  .sheet {
    position: relative; width: 1200px; height: 900px;
    display: flex; flex-direction: column; align-items: center; justify-content: center; gap: 40px;
  }
  .card {
    position: relative; width: 700px; height: 400px;
    background: linear-gradient(160deg, var(--card-edge), var(--card));
    box-shadow: 0 10px 30px rgba(0,0,0,.45);
    overflow: hidden;
  }
  /* front */
  .card-front { display: flex; }
  .portrait {
    width: 290px; height: 100%;
    background: linear-gradient(90deg, var(--photo-green) 0%, #6f7a52 25%, #d8d2c8 45%, var(--photo-warm) 75%, #b89773 100%);
  }
  .accent-stripe { width: 6px; height: 100%; background: var(--magenta); }
  .front-brand { flex: 1; display: flex; align-items: center; justify-content: center; }
  .brand { display: flex; flex-direction: column; align-items: center; gap: 18px; }
  .brand-name {
    display: flex; align-items: center; gap: 12px; white-space: nowrap;
    font-family: "Libre Baskerville", serif; font-size: 36px; color: var(--logo-grey); line-height: 1;
  }
  .brand-dot { width: 28px; height: 28px; border-radius: 50%; background: var(--logo-grey); flex: none; }
  .tagline {
    font-family: "Didact Gothic", sans-serif; font-size: 24px; color: var(--tagline-grey);
    letter-spacing: .5px; white-space: nowrap;
  }
  /* back */
  .card-back { display: flex; align-items: center; padding: 0 30px 0 24px; }
  .back-brand { width: 300px; display: flex; justify-content: center; flex: none; }
  .back-brand .brand-name { font-size: 29px; }
  .back-brand .brand-dot { width: 24px; height: 24px; }
  .back-brand .tagline { font-size: 22px; }
  .divider { width: 2px; height: 170px; background: var(--ink); margin: 0 24px 0 14px; flex: none; }
  .contact { font-family: "Didact Gothic", sans-serif; color: var(--ink); font-size: 16px; line-height: 1.4; white-space: nowrap; }
  .contact-name {
    font-family: "Libre Baskerville", serif; color: var(--magenta); font-size: 19px;
    letter-spacing: 1.5px; text-transform: uppercase; line-height: 1.2;
  }
  .credentials { margin-bottom: 12px; }
  .address { margin-bottom: 12px; }
  .contact-line { display: flex; align-items: center; gap: 9px; }
  .contact-line svg { width: 12px; height: 12px; flex: none; }
  .highlight { color: var(--magenta); }
  .social { display: flex; align-items: center; gap: 8px; margin-top: 18px; font-size: 14px; }
  .social-square { width: 18px; height: 18px; background: var(--social); border-radius: 2px; }
</style>
</head>
<body>
<main class="sheet">
  <section class="card card-front">
    <div class="portrait" role="img" aria-label="Portrait photograph of the coach leaning against a brick wall beside greenery"></div>
    <div class="accent-stripe"></div>
    <div class="front-brand">
      <div class="brand">
        <div class="brand-name">Lucinda Parvell<span class="brand-dot"></span></div>
        <div class="tagline">• spirited living •</div>
      </div>
    </div>
  </section>

  <section class="card card-back">
    <div class="back-brand">
      <div class="brand">
        <div class="brand-name">Lucinda Parvell<span class="brand-dot"></span></div>
        <div class="tagline">• spirited living •</div>
      </div>
    </div>
    <div class="divider"></div>
    <div class="contact">
      <div class="contact-name">Lucinda Parvell</div>
      <div class="credentials">CHN, RNCP, BSc</div>
      <div class="address">418 Maple Ridge Rd., Kingsford<br>ON, K0L 3B6</div>
      <div class="contact-line">
        <svg viewBox="0 0 12 12"><path d="M2.5 1 L4.5 1 L5 3.5 L3.8 4.4 Q5 7 7.6 8.2 L8.5 7 L11 7.5 L11 9.5 Q10.5 11 9 11 Q1 10 1 2.5 Q1 1 2.5 1 Z" fill="var(--magenta)"/></svg>
        519-362-7015
      </div>
      <div class="contact-line">
        <svg viewBox="0 0 12 12"><rect x="1" y="2.5" width="10" height="7" fill="none" stroke="var(--magenta)" stroke-width="1.2"/><path d="M1 2.5 L6 6.5 L11 2.5" fill="none" stroke="var(--magenta)" stroke-width="1.2"/></svg>
        lucinda@lucindaparvell.com
      </div>
      <div class="contact-line">
        <svg viewBox="0 0 12 12"><circle cx="6" cy="6" r="5" fill="none" stroke="var(--magenta)" stroke-width="1.1"/><ellipse cx="6" cy="6" rx="2.2" ry="5" fill="none" stroke="var(--magenta)" stroke-width="1"/><path d="M1 6 H11" stroke="var(--magenta)" stroke-width="1"/></svg>
        <span>www.<span class="highlight">lucindaparvell</span>.com</span>
      </div>
      <div class="social"><span class="social-square"></span>@lucindaparvell</div>
    </div>
  </section>
</main>
</body>
</html>
```